BRQ-Bluefield Ridge Quorum LLC (Business Cards)

The attached design was selected as the logo for our company. I need to proceed on creating our business cards.

Teodoro

Target Market(s)

This is a technology and Project Management company. The audience will be business decision makers of a diversity of companies.

Industry/Entity Type

Business

Font styles to use
Sans Serif
Script

Colors

Designer to choose colors to be used in the design.

```html
<!DOCTYPE html>
<html lang="en">
<head>
<meta charset="utf-8">
<title>Bluefield Ridge Quorum – Business Card</title>
<link rel="stylesheet" href="https://fonts.googleapis.com/css2?family=Quicksand:wght@500&family=Cinzel:wght@400&family=Open+Sans:wght@400&display=swap">
<style>
  :root {
    --backdrop: #e6e4e1;
    --card: #ffffff;
    --card-shade: #f1f1f1;
    --brand-red: #9b1c22;
    --ink: #1e1e1e;
    --ink-soft: #3a3a3a;
    --icon-fill: #2b2b2b;
    --icon-text: #d9d9d9;
  }
  * { margin: 0; padding: 0; box-sizing: border-box; }
  html, body {
    width: 1200px; height: 675px; overflow: hidden;
    background: var(--backdrop);
  }
  .card {
    position: absolute; left: 100px; top: 52px;
    width: 1000px; height: 571px;
    background: radial-gradient(ellipse at 40% 50%, var(--card) 40%, var(--card-shade) 100%);
    box-shadow: 0 6px 24px rgba(0,0,0,0.18);
  }
  .brand {
    position: absolute; left: 50px; top: 150px;
    display: flex; align-items: center; gap: 22px;
  }
  .brand-dot {
    width: 150px; height: 150px; border-radius: 50%;
    background: var(--brand-red);
    flex: none;
  }
  .brand-name {
    font-family: "Quicksand", sans-serif; font-weight: 500;
    font-size: 36px; line-height: 1.05; color: var(--ink);
    letter-spacing: 0.5px;
  }
  .person {
    position: absolute; left: 560px; top: 62px;
    font-family: "Cinzel", serif; color: var(--ink-soft);
  }
  .person-name { font-size: 34px; letter-spacing: 1px; }
  .person-role { font-size: 32px; margin-left: 12px; margin-top: 10px; }
  .contact {
    position: absolute; left: 590px; top: 300px;
    list-style: none;
    font-family: "Open Sans", sans-serif; font-size: 21px;
    text-transform: uppercase; color: var(--ink);
  }
  .contact-item { display: flex; align-items: flex-start; gap: 8px; line-height: 1.3; margin-bottom: 6px; }
  .contact-icon { flex: none; margin-top: 5px; }
  .contact-icon circle { fill: var(--icon-fill); }
  .contact-icon text {
    fill: var(--icon-text); font-family: "Open Sans", sans-serif;
    font-size: 11px; text-anchor: middle;
  }
</style>
</head>
<body>
  <main class="card">
    <div class="brand">
      <div class="brand-dot"></div>
      <div class="brand-name">Bluefield<br>Ridge<br>Quorum</div>
    </div>

    <div class="person">
      <p class="person-name">Marcus Delvane</p>
      <p class="person-role">CEO</p>
    </div>

    <ul class="contact">
      <li class="contact-item">
        <svg class="contact-icon" width="20" height="20" viewBox="0 0 20 20"><circle cx="10" cy="10" r="10"/><text x="10" y="14">A</text></svg>
        <span>214-60 Harlow Street<br>North Fitzroy VIC 8310</span>
      </li>
      <li class="contact-item">
        <svg class="contact-icon" width="20" height="20" viewBox="0 0 20 20"><circle cx="10" cy="10" r="10"/><text x="10" y="14">P</text></svg>
        <span>+61 3 5550 1287</span>
      </li>
      <li class="contact-item">
        <svg class="contact-icon" width="20" height="20" viewBox="0 0 20 20"><circle cx="10" cy="10" r="10"/><text x="10" y="14">P</text></svg>
        <span>+61 3 5550 1287</span>
      </li>
      <li class="contact-item">
        <svg class="contact-icon" width="20" height="20" viewBox="0 0 20 20"><circle cx="10" cy="10" r="10"/><text x="10" y="14">E</text></svg>
        <span>info@bluefieldrq.com</span>
      </li>
      <li class="contact-item">
        <svg class="contact-icon" width="20" height="20" viewBox="0 0 20 20"><circle cx="10" cy="10" r="10"/><text x="10" y="14">W</text></svg>
        <span>www.bluefieldrq.com</span>
      </li>
    </ul>
  </main>
</body>
</html>
```